French version of popular website and translation

Translate existing website
Design simple copy of existing website in french

Logo stays the same
Content and pages stay the same

We just need to translate the website(s) and provide functional version of french website.

Please goto www.plivok.ca and new.plivok.ca

These 2 websites need to be copied, and 1 new french website needs to be created with existing content

We will then create a new website

www.plivok.ca/fr

There our new French website will be accessible, and our french team will be able to update it

Coding

Number of Pages Required

5+ page

Font styles to use
Sans Serif

Colors
cee9f5
cadf82
86cfc6
9bcb3b
aeded8
33b8a4
0dac94
00a990

Requirements
Must have
• Existing logo
• Existing photos from charities
• Existing information about our organization
Nice to have
• www.plivok.ca ( copy all pages with text and content)
• new.plivok.ca ( copy all pages with text and content)

```html
<!DOCTYPE html>
<html lang="fr">
<head>
<meta charset="utf-8">
<title>Plivok Recycling Association – Accueil</title>
<link rel="stylesheet" href="https://fonts.googleapis.com/css2?family=Open+Sans:wght@400;600;700;800&display=swap">
<style>
:root{
  --green:#8dc63f;
  --green-light:#9bcb3b;
  --green-soft:#cadf82;
  --teal:#00a990;
  --teal-mid:#33b8a4;
  --dark:#2f2f2f;
  --text:#555;
  --muted:#8a8a8a;
  --grey-bg:#ededed;
  --grey-cell:#f3f3f3;
  --grey-dark:#e4e4e4;
  --forest:#1f3d1c;
  --white:#fff;
}
*{box-sizing:border-box;margin:0;padding:0}
html,body{width:1200px;height:4296px;overflow:hidden}
body{font-family:"Open Sans",Arial,sans-serif;color:var(--text);background:var(--white);position:relative}
/* top bar */
.topbar{position:absolute;top:0;left:0;width:1200px;height:30px;border-bottom:1px solid #eee;font-size:11px;color:var(--muted)}
.topbar .social{position:absolute;left:20px;top:9px;display:flex;gap:24px}
.topbar .social span{width:12px;height:12px;border-radius:50%;background:#b5b5b5;display:block}
.topbar .contact{position:absolute;left:330px;top:8px;display:flex;gap:30px}
.topbar .contact b{color:#e55;font-weight:400}
.topbar .lang{position:absolute;right:20px;top:7px;display:flex;gap:8px;align-items:center}
.topbar .lang em{font-style:normal;color:#e55}
.topbar .lang span{background:var(--green);color:#fff;padding:1px 6px;border-radius:2px;font-size:10px}
/* header */
.header{position:absolute;top:30px;left:0;width:1200px;height:108px}
.brand{position:absolute;left:34px;top:36px;display:flex;align-items:center;gap:12px}
.brand-mark{width:46px;height:46px;border-radius:50%;background:var(--green)}
.brand-name{font-size:17px;color:var(--teal);font-weight:600}
.nav{position:absolute;right:20px;top:45px;display:flex;font-size:12px;font-weight:700;color:var(--dark)}
.nav span{padding:0 14px;border-left:1px solid #ddd}
.nav span:first-child{border-left:none}
/* hero */
.hero{position:absolute;top:138px;left:0;width:1200px;height:658px;background:linear-gradient(180deg,#8c8c88,#5a5752 60%,#3b3a38)}
.hero-banner{position:absolute;left:0;top:0;width:372px;height:658px;background:linear-gradient(180deg,#e7f1f4,#cfe4ec)}
.hero-banner .mark{position:absolute;left:40px;top:50px;width:130px;height:130px;border-radius:50%;background:var(--green)}
.hero-banner .mark-name{position:absolute;left:190px;top:100px;font-size:30px;font-weight:700;color:var(--teal)}
.hero-banner h2{position:absolute;left:20px;top:200px;font-size:36px;line-height:1.15;color:var(--teal);font-weight:400}
.hero-banner .photo{position:absolute;left:20px;top:370px;width:240px;height:120px;background:#7b8a95}
.hero-banner p{position:absolute;left:20px;top:510px;width:300px;font-size:11px;color:#4a6b7a}
.hero-banner .foot{position:absolute;left:0;bottom:0;width:372px;height:70px;background:#1f6c8a;color:#fff;font-size:26px;padding:18px 20px}
.hero-caption{position:absolute;left:600px;top:349px;width:600px;height:63px;background:rgba(255,255,255,.92);font-size:40px;color:var(--dark);padding:4px 0 0 14px;font-weight:400}
/* advantages */
.adv{position:absolute;top:796px;left:0;width:1200px;height:694px}
.adv-head{position:absolute;left:372px;top:6px;width:828px;height:68px;background:var(--green);color:#fff;font-weight:700;font-size:19px;letter-spacing:1px;text-align:center;line-height:68px}
.cell{position:absolute;text-align:center;padding:0 26px}
.cell h3{font-size:14px;font-weight:700;color:var(--dark);margin:8px 0 12px;text-transform:uppercase;letter-spacing:.3px}
.cell p{font-size:11.5px;line-height:1.55;color:var(--text)}
.cell svg{display:block;margin:0 auto}
.c-exp{left:0;top:0;width:372px;height:694px;padding:0 40px;background:var(--white)}
.c-exp svg{margin-top:140px}
.c-exp h3{margin-top:80px;font-size:17px}
.c-exp p{text-align:left}
.c-comm{left:372px;top:74px;width:414px;height:261px;background:var(--grey-cell);padding-top:40px}
.c-sec{left:786px;top:74px;width:414px;height:261px;background:var(--white);padding-top:40px}
.c-sup{left:372px;top:335px;width:272px;height:359px;background:var(--white);padding-top:46px}
.c-full{left:644px;top:335px;width:244px;height:359px;background:var(--grey-dark);padding-top:46px}
.c-comp{left:888px;top:335px;width:312px;height:359px;background:var(--grey-cell);padding-top:46px}
/* video */
.video{position:absolute;top:1518px;left:0;width:1200px;height:358px;background:#1b1b1b;overflow:hidden}
.video-media{position:absolute;left:0;top:0;width:760px;height:358px;background:linear-gradient(120deg,#4d7a1d,#9fd04a 45%,#3d6a18);clip-path:polygon(0 0,100% 0,88% 100%,0 100%)}
.video h2{position:absolute;left:190px;top:118px;font-size:48px;color:#fff;font-weight:400}
.video .sub{position:absolute;left:100px;top:182px;font-size:15px;color:#fff;font-weight:600}
.video .play{position:absolute;left:258px;top:230px;width:80px;height:80px;border-radius:50%;background:rgba(255,255,255,.35)}
.video-text{position:absolute;left:758px;top:48px;width:420px;color:#fff}
.video-text h3{font-size:19px;font-weight:700;line-height:1.25;margin-bottom:18px}
.video-text p{font-size:12px;line-height:1.55;color:#ddd}
.btn-outline{display:inline-block;margin-top:24px;border:2px solid var(--green);color:#fff;font-size:12px;font-weight:600;padding:6px 10px;border-radius:3px}
/* highlights */
.hl{position:absolute;top:1876px;left:0;width:1200px;height:553px;background:var(--grey-bg)}
.hl-card{position:absolute;width:352px;height:263px;background:var(--white)}
.hl-card .img{position:absolute;left:45px;top:16px;width:262px;height:200px}
.hl-card span{position:absolute;left:0;bottom:14px;width:100%;text-align:center;font-size:14px;font-weight:600;color:var(--dark)}
.hl-side{position:absolute;left:752px;top:0;width:448px;height:553px;background:var(--white);text-align:center}
.hl-side svg{margin-top:150px}
.hl-side h3{color:var(--teal-mid);font-size:19px;font-weight:400;line-height:1.3;margin:30px 60px 22px;text-transform:uppercase}
.hl-side p{font-size:12px;color:var(--dark);font-weight:600;margin:0 110px}
/* facts */
.facts{position:absolute;top:2429px;left:0;width:1200px;height:335px;background:linear-gradient(180deg,#1d3a1b,#2d5a22 60%,#1f3d1c)}
.facts h2{position:absolute;top:0;left:0;width:1200px;height:86px;line-height:86px;text-align:center;color:#fff;font-size:22px;font-weight:700;letter-spacing:1px;border-bottom:1px solid rgba(255,255,255,.35)}
.fact{position:absolute;top:128px;width:300px;text-align:center;color:#fff}
.fact svg{display:block;margin:0 auto 12px}
.fact em{font-style:normal;display:block;font-size:16px}
.fact b{display:block;font-size:36px;font-weight:400;margin-top:10px}
/* certifications */
.cert{position:absolute;top:2764px;left:0;width:1200px;height:315px;text-align:center}
.cert h2{margin-top:60px;color:var(--green);font-size:19px;font-weight:600;letter-spacing:1px}
.cert p{margin:30px auto 0;width:900px;font-size:12px}
.badges{display:flex;justify-content:center;gap:70px;margin-top:30px}
.badges span{display:block;width:90px;height:44px;background:#dcdcdc;border-radius:4px}
/* testimonial */
.testi{position:absolute;top:3079px;left:0;width:1200px;height:243px;background:var(--grey-bg)}
.testi .card{position:absolute;left:256px;top:66px;width:834px;height:100px;background:var(--white);padding:20px 40px 0 50px;font-size:13px;line-height:1.5;color:var(--dark)}
.testi .card::before{content:"\201C";position:absolute;left:18px;top:6px;font-size:44px;font-weight:700;color:var(--dark)}
.testi .who{position:absolute;left:256px;top:180px;font-size:14px;font-weight:700;font-style:italic;color:var(--dark)}
.dots{position:absolute;left:540px;top:214px;display:flex;gap:5px}
.dots span{width:10px;height:10px;border-radius:50%;border:1px solid #999}
.dots span:first-child{background:#999}
/* CTA */
.cta{position:absolute;top:3337px;left:0;width:1200px;height:300px;background:linear-gradient(90deg,#6ea433,#8dc63f 60%,#7db538)}
.cta h2{position:absolute;left:30px;top:92px;color:#fff;font-size:22px;font-weight:700}
.cta p{position:absolute;left:30px;top:140px;width:800px;font-size:12px;color:#fff;line-height:1.55}
.cta .btn{position:absolute;right:30px;top:80px;width:260px;height:46px;background:#2c2c2c;color:#fff;border:2px solid #fff;border-radius:4px;text-align:center;line-height:42px;font-size:15px}
/* footer */
.footer{position:absolute;top:3652px;left:0;width:1200px;height:587px}
.fcol{position:absolute;top:46px;font-size:12px;color:var(--text)}
.fcol h4{display:flex;align-items:center;gap:10px;font-size:13px;font-weight:700;color:var(--teal);letter-spacing:.5px;margin-bottom:20px}
.fcol h4 i{width:26px;height:26px;border-radius:50%;background:var(--teal);display:block}
.fcol li{list-style:none;margin-bottom:12px;padding-left:12px;position:relative;line-height:1.4}
.fcol li::before{content:"-";position:absolute;left:0}
.contact-line{display:flex;align-items:center;gap:10px;margin-bottom:16px}
.contact-line i{width:22px;height:22px;border-radius:50%;border:1px solid #bbb;display:block}
.insta{display:grid;grid-template-columns:repeat(5,44px);gap:4px}
.insta span{height:44px;background:#8a8a80;display:block}
.insta span:nth-child(3n){background:#b9b0a0}
.insta span:nth-child(4n){background:#5d6b73}
.fbtn{display:block;width:90px;margin:14px auto 0;background:#444;color:#fff;text-align:center;font-size:11px;padding:4px}
.fbtn2{display:block;width:140px;margin:8px auto 0;background:#3a7bbf;color:#fff;text-align:center;font-size:11px;padding:4px}
.fb{width:260px;height:370px;border:1px solid #ddd;background:#fafafa;padding:8px}
.fb .top{height:60px;background:#dfe6df}
.fb .title{font-size:15px;font-weight:700;color:var(--dark);margin-top:12px}
.fb .img{height:200px;background:#c7d1c0;margin-top:10px}
.tweet{margin-bottom:22px;line-height:1.45}
.tweet b{color:var(--teal);font-weight:400}
.footer-brand{position:absolute;left:470px;top:506px;display:flex;align-items:center;gap:10px}
.footer-brand i{width:40px;height:40px;border-radius:50%;background:var(--green);display:block}
.footer-brand span{color:var(--teal);font-size:16px;font-weight:600}
.copyright{position:absolute;top:4239px;left:0;width:1200px;height:57px;background:var(--green);color:#fff;font-size:10px;font-weight:700;text-align:center;line-height:57px;letter-spacing:.5px}
</style>
</head>
<body>

<div class="topbar">
  <div class="social"><span></span><span></span><span></span><span></span><span></span><span></span></div>
  <div class="contact"><span>1-877-555-0142</span><b>info@plivok.ca</b></div>
  <div class="lang"><em>Live Chat</em><span>EN</span></div>
</div>

<header class="header">
  <div class="brand"><div class="brand-mark"></div><div class="brand-name">plivok recycling association</div></div>
  <nav class="nav"><span>ABOUT US</span><span>BOOK A PICKUP</span><span>DEPOTS</span><span>GET INVOLVED</span><span>CALENDAR</span><span>DATA SECURITY</span><span>CHARITIES</span><span>MEDIA</span><span>CONTACT</span></nav>
</header>

<section class="hero" role="img" aria-label="Photo de l'équipe de recyclage devant l'entrepôt">
  <div class="hero-banner">
    <div class="mark"></div><div class="mark-name">plivok.ca</div>
    <h2>Support your community and environment.</h2>
    <div class="photo" role="img" aria-label="Photo d'un don d'ordinateurs à une école"></div>
    <p>Donate your old computers to PLIVOK, they might just change someone's life.</p>
    <div class="foot">The whole new PLIVOK</div>
  </div>
  <div class="hero-caption">Computer recycling experts</div>
</section>

<section class="adv">
  <div class="adv-head">LES AVANTAGES DE CHOISIR PLIVOK</div>
  <div class="cell c-exp">
    <svg width="90" height="80" viewBox="0 0 90 80"><path d="M6 42 L32 68 L84 10" fill="none" stroke="#111" stroke-width="14"/></svg>
    <h3>Expérience</h3>
    <p>PLIVOK est un chef de file du recyclage et de la réutilisation des ordinateurs et des appareils électroniques au Canada depuis 2004. Nous avons fait nos preuves en fournissant des services ministériels fiables, rapides et sécurisés.</p>
  </div>
  <div class="cell c-comm">
    <svg width="30" height="26" viewBox="0 0 30 26"><circle cx="15" cy="7" r="5" fill="#333"/><circle cx="5" cy="10" r="3.5" fill="#333"/><circle cx="25" cy="10" r="3.5" fill="#333"/><path d="M6 26c0-7 4-12 9-12s9 5 9 12z" fill="#333"/></svg>
    <h3>Implication de la communauté</h3>
    <p>Nous nous sommes engagés à fournir de l'équipement remis à neuf gratuitement aux organismes de bienfaisance locaux. En travaillant avec nous, vous pouvez vous sentir bien en sachant que votre ancien équipement pourrait profiter à une famille canadienne moins fortunée. Consultez notre page d'événements.</p>
  </div>
  <div class="cell c-sec">
    <svg width="24" height="28" viewBox="0 0 24 28"><path d="M12 0 L24 4 V13 C24 21 18 26 12 28 C6 26 0 21 0 13 V4z" fill="#333"/><path d="M12 3 V25 C7 23 3 19 3 13 V6z" fill="#fff"/></svg>
    <h3>Sécurité</h3>
    <p>À chaque étape du processus de récupération, de la collecte à l'utilisation secondaire, PLIVOK garantit la sécurité des données de vos informations sensibles. Utilisant le logiciel brasure software leader de l'industrie et les destructeurs de disques durs physiques puissants, vous pouvez être assuré que votre équipement est entre de bonnes mains.</p>
  </div>
  <div class="cell c-sup">
    <svg width="28" height="30" viewBox="0 0 28 30"><circle cx="14" cy="13" r="10" fill="#333"/><path d="M3 13a11 11 0 0 1 22 0" fill="none" stroke="#333" stroke-width="3"/><rect x="0" y="12" width="5" height="9" rx="2" fill="#333"/><rect x="23" y="12" width="5" height="9" rx="2" fill="#333"/><path d="M6 30c0-5 4-7 8-7s8 2 8 7z" fill="#333"/></svg>
    <h3>Grand soutien</h3>
    <p>Avec des dizaines de membres du personnel qualifiés prêts à répondre à vos questions, nous ne laisserons pas votre question ou votre préoccupation sans réponse.</p>
  </div>
  <div class="cell c-full">
    <svg width="30" height="30" viewBox="0 0 30 30"><circle cx="14" cy="16" r="12" fill="none" stroke="#333" stroke-width="3"/><circle cx="14" cy="16" r="6" fill="none" stroke="#333" stroke-width="3"/><circle cx="14" cy="16" r="2" fill="#333"/><path d="M14 16 L28 2 M24 2h4v4" stroke="#333" stroke-width="2.5" fill="none"/></svg>
    <h3>Services complets</h3>
    <p>Nous avons une gamme de services pour couvrir vos besoins informatiques en matière de retraite. Collecte d'équipement, destruction de données sur site ou hors site (matériel et logiciel), rapports détaillés, adhésions à valeur ajoutée et diverses options de collecte d'équipement sur site.</p>
  </div>
  <div class="cell c-comp">
    <svg width="30" height="28" viewBox="0 0 30 28"><rect x="1" y="1" width="28" height="19" rx="2" fill="#333"/><rect x="4" y="4" width="22" height="13" fill="#fff"/><rect x="12" y="20" width="6" height="5" fill="#333"/><rect x="7" y="25" width="16" height="3" fill="#333"/></svg>
    <h3>Pas seulement des ordinateurs</h3>
    <p>PLIVOK acceptera presque n'importe quel type d'électronique que vous avez. Des câbles aux jeux d'arcade en taille réelle, nous pouvons gérer la plupart des appareils électroniques. Nous pouvons même fournir des bacs de collecte, nous assurerons même de les rétablir.</p>
  </div>
</section>

<section class="video">
  <div class="video-media" role="img" aria-label="Image verte floue de bureaux et d'écrans"></div>
  <h2>PLIVOK VIDEO</h2>
  <div class="sub">Computer Electronics Recycling and Reuse in Canada</div>
  <div class="play"><svg width="80" height="80" viewBox="0 0 80 80"><path d="M32 24 L58 40 L32 56z" fill="#fff"/></svg></div>
  <div class="video-text">
    <h3>RÉUTILISATION INFORMATIQUE<br>ET ÉLECTRONIQUE</h3>
    <p>La Plivok Recycling Association (PLIVOK) est une organisation à but non lucratif qui recycle les déchets électroniques inutiles depuis 2004. Nous réduisons la contribution environnementale défavorable en recyclant, en réaffectant et en faisant don de matériel électronique et d'autres équipements informatiques. Avec un certain nombre de points de dépôt à travers le Canada basés principalement à Calgary, Edmonton, Vancouver, Saskatoon, Toronto et Winnipeg, et un service de ramassage électronique.</p>
    <span class="btn-outline">Apprendre Encore Plus</span>
  </div>
</section>

<section class="hl">
  <div class="hl-card" style="left:14px;top:14px"><div class="img" role="img" aria-label="Photo de la remise d'un don en 2017" style="background:#9a8f86"></div><span>2017 HIGHLIGHTS</span></div>
  <div class="hl-card" style="left:386px;top:14px"><div class="img" role="img" aria-label="Photo de l'événement 2016" style="background:#4a5a78"></div><span>2016 HIGHLIGHTS</span></div>
  <div class="hl-card" style="left:14px;top:290px"><div class="img" role="img" aria-label="Photo d'un camion de collecte en 2015" style="background:#b7bdb4"></div><span>2015 HIGHLIGHTS</span></div>
  <div class="hl-card" style="left:386px;top:290px"><div class="img" role="img" aria-label="Photo d'une cérémonie de 2014" style="background:#5a5048"></div><span>2014 HIGHLIGHTS</span></div>
  <div class="hl-side">
    <svg width="110" height="90" viewBox="0 0 110 90"><path d="M10 35 h18 l45-28 v76 l-45-28 h-18z" fill="none" stroke="#33b8a4" stroke-width="8" stroke-linejoin="round"/><path d="M24 55 l8 30 h12 l-6-28" fill="none" stroke="#33b8a4" stroke-width="7"/><path d="M86 30 l16-10 M88 45 h18 M86 60 l16 10" stroke="#33b8a4" stroke-width="7"/></svg>
    <h3>Dernier ordinateur et nouvelles de recyclage électronique et dons</h3>
    <p>Résumé des dons informatiques et recyclage des événements par année</p>
  </div>
</section>

<section class="facts">
  <h2>FAITS INCROYABLES</h2>
  <div class="fact" style="left:30px"><svg width="52" height="40" viewBox="0 0 52 40"><circle cx="26" cy="8" r="6" fill="#fff"/><circle cx="10" cy="12" r="5" fill="#fff"/><circle cx="42" cy="12" r="5" fill="#fff"/><path d="M18 40V22h16v18zM3 40V24h14v16zM35 40V24h14v16z" fill="#fff"/></svg><em>Charités heureuses</em><b>150</b></div>
  <div class="fact" style="left:300px"><svg width="52" height="40" viewBox="0 0 52 40"><rect x="8" y="4" width="36" height="24" fill="none" stroke="#fff" stroke-width="3"/><path d="M2 34h48l-4 4H6z" fill="#fff"/></svg><em>Ordinateurs partagés</em><b>2500</b></div>
  <div class="fact" style="left:590px"><svg width="52" height="40" viewBox="0 0 52 40"><rect x="10" y="2" width="32" height="36" rx="3" fill="none" stroke="#fff" stroke-width="3"/><circle cx="26" cy="17" r="9" fill="none" stroke="#fff" stroke-width="2.5"/><circle cx="26" cy="17" r="2" fill="#fff"/></svg><em>Disques durs déchiquetés</em><b>748000</b></div>
  <div class="fact" style="left:880px"><svg width="52" height="40" viewBox="0 0 52 40"><path d="M10 10h32l-3 30H13z" fill="none" stroke="#fff" stroke-width="3"/><path d="M6 10h40M20 4h12v6" stroke="#fff" stroke-width="3" fill="none"/></svg><em>KG's Décharge évitée</em><b>1100000</b></div>
</section>

<section class="cert">
  <h2>CERTIFICATIONS ET ACCRÉDITATIONS</h2>
  <p>Afin de rester informé et d'assurer une participation maximale dans la communauté du recyclage, la Plivok Recycling Association maintient des adhésions avec des associations de recyclage à travers le Canada.</p>
  <div class="badges"><span></span><span></span><span></span><span></span><span></span><span></span></div>
</section>

<section class="testi">
  <div class="card">It is our experience that they deliver what they promise and to the highest standard...Their customer service is impeccable and as an organization that values Sustainability and Corporate Social Responsibility, I couldn't think of a better partner than PLIVOK.</div>
  <div class="who">Major Canadian Automobile Association</div>
  <div class="dots"><span></span><span></span><span></span><span></span></div>
</section>

<section class="cta">
  <h2>ÊTES-VOUS PRET A EMPOWERER LES AUTRES? FAITES UN DON</h2>
  <p>Les dons d'équipement inutilisé aident à garder les déchets électroniques éloignés des décharges. Grâce à nos programmes de réutilisation, vos dons sont revalorisés et reçoivent une seconde mission, là où l'électronique ne peut absolument pas être réutilisée, nous la recyclerons.</p>
  <div class="btn">Réserver un Pick-up</div>
</section>

<footer class="footer">
  <div class="fcol" style="left:34px;width:230px">
    <h4>CONTACT</h4>
    <div class="contact-line"><i></i>1-877-555-0142</div>
    <div class="contact-line"><i></i>info@plivok.ca</div>
    <h4 style="margin-top:26px">NEWS</h4>
    <ul>
      <li>Edmonton Donation Day</li>
      <li>Centre Nordique Receives a Donation</li>
      <li>Parkvale Centre - Kicking off Waste Reduction Week!</li>
      <li>The Town of Elmsvale's Community Cleanup</li>
      <li>PLIVOK Helps a Foster Parent Receive a Donation</li>
    </ul>
  </div>
  <div class="fcol" style="left:314px;width:236px">
    <h4><i></i>INSTAGRAM</h4>
    <div class="insta" role="img" aria-label="Grille de photos récentes">
      <span></span><span></span><span></span><span></span><span></span><span></span><span></span><span></span><span></span><span></span><span></span><span></span><span></span><span></span><span></span><span></span><span></span><span></span><span></span><span></span>
    </div>
    <span class="fbtn">Load More</span>
    <span class="fbtn2">Follow on Instagram</span>
  </div>
  <div class="fcol" style="left:574px;width:270px">
    <h4><i></i>FACEBOOK</h4>
    <div class="fb">
      <div class="top" role="img" aria-label="Bannière de la page"></div>
      <div class="title">PLIVOK Partnering wi...</div>
      <div style="font-size:11px">The Plivok Recycling Ass...</div>
      <div class="img" role="img" aria-label="Photo de publication"></div>
      <div style="font-size:11px;margin-top:10px">Like · Comment · Share</div>
    </div>
  </div>
  <div class="fcol" style="left:900px;width:270px">
    <h4><i></i>TWITTER</h4>
    <div class="tweet"><b>@plivokrecycle</b> Thinking about getting rid of old #electronics that are cluttering your offices? #Donate them to those who need it most!</div>
    <div class="tweet"><b>@plivokcalgary</b> Thinking about getting rid of old #electronics that are cluttering your offices? #Donate them to those who need it most!</div>
    <div class="tweet"><b>@plivokedm</b> PLIVOK refurbishes and donates electronics to people in need. Help us build a better and greener #future by donating old equipment!</div>
  </div>
  <div class="footer-brand"><i></i><span>plivok recycling association</span></div>
</footer>

<div class="copyright">COPYRIGHT © 2017 PLIVOK RECYCLING ASSOCIATION. ALL RIGHTS RESERVED</div>

</body>
</html>
```